Website Design for two swimming school brands

Looking for a modern, engaging website design for my new business Every Stroke Water Learning. Within that business I have two current brands:
Every Stroke Swim and Yard Paddle
My current website (www.yardpaddle.net) has most of the info you'll need. Feel free to also use my socials for content.
Looking for someone to do the initial design/setup and then hand over full control to me with no ongoing fees or charges (except for hosting), and I'm responsible for all future changes. Ideally made and then can be edited in google sites but open to other options.

Website requirements are quite simple for both pages.
For the Yard Paddle page, I'd like the same info and features that are on my current website presented in a fresh way.
For the Every Stroke page, I'd like to see your concepts for design and possible sections, but it'll be roughly the same as the yard paddle one. I will upload a document soon for text and sections and other information to go on the Every stroke swim page.

For clarity the difference between the business' is one goes out to people's home pools and the other hires out lane space in public pool to conduct lessons.
I'd like a lighter theme for the Yard Paddle Website and a Darker one for the Every Stroke.
Both pages needs to be accessible with picture descriptions for screen reader and other similar features.

I currently use Bookora for all my inquiry, booking and payment functions so the website would need to be compatible with their widgets.

Have a look at the MockUp v2 or the business card design to get the concept of two different brandings working together.

Some text from the Every Stroke Swim Page can be found in this document:
https://docs.example-files.net/document/d/7QpaLmRvXc2TnWb8KdYs4FgHe9JuZoNi3VcXaBt/edit?usp=sharing
-
Feel free to ask any further questions.
Updates

Target Market(s)

Families and disability service providers

Industry/Entity Type

Sports and Recreation

Coding

Coded - Design and coding required

Number of Pages Required

4 page

Requirements
Must have
• Engaging design, ability to put in widgets into website, cross links between two business
Nice to have
• Common elements across the two pages but also points of difference

```html
<!DOCTYPE html>
<html lang="en">
<head>
<meta charset="utf-8">
<title>Yard Paddle – Mobile Swimming Lessons</title>
<link href="https://fonts.googleapis.com/css2?family=Montserrat:ital,wght@0,400;0,500;0,600;0,700;1,400&display=swap" rel="stylesheet">
<style>
:root{
  --blue:#1b8fd6;
  --blue-dark:#1273b8;
  --teal:#20a39e;
  --green:#2bb6a8;
  --ink:#333b44;
  --muted:#6b7480;
  --line:#e3e8ee;
  --white:#ffffff;
}
*{box-sizing:border-box;margin:0;padding:0}
html,body{width:1200px;height:4751px;overflow:hidden}
body{position:relative;background:var(--white);font-family:'Montserrat',sans-serif;color:var(--ink)}
.abs{position:absolute}
.center{text-align:center}
svg.band{position:absolute;left:0;width:1200px}

/* top bar */
.topbar{left:0;top:0;width:1200px;height:35px;background:var(--blue);color:var(--white);font-size:11px;font-weight:700;letter-spacing:.3px}
.topbar .follow{left:112px;top:11px}
.topbar .social{top:6px;width:23px;height:23px;border-radius:50%;background:var(--white)}
.topbar .acct{top:0;height:35px;line-height:35px;padding:0 18px;border-left:1px solid rgba(255,255,255,.35)}

/* header */
.brand{font-weight:700;color:var(--teal);letter-spacing:.5px}
.brand-mark{border-radius:6px;background:var(--teal)}
.contact-mini{font-size:12px;font-weight:600;color:var(--ink)}
.contact-mini small{display:block;font-size:9px;color:var(--blue);font-weight:600}
.contact-mini .ico{position:absolute;left:-28px;top:3px;width:22px;height:22px;border-radius:50%;background:var(--blue)}
.lang{left:997px;top:68px;width:90px;height:35px;border:1px solid #cfd6de;border-radius:3px;font-size:11px;font-weight:700;line-height:33px;padding-left:34px}
.lang i{position:absolute;left:12px;top:11px;width:16px;height:11px;background:linear-gradient(#c8102e 0 33%,#fff 33% 66%,#1f3e8c 66%)}
.nav a{position:absolute;top:126px;font-size:12px;font-weight:500;color:var(--ink);text-decoration:none}
.nav a.active{color:var(--blue)}
.nav a.active:after{content:"";position:absolute;left:0;right:0;bottom:-7px;height:2px;background:var(--blue)}

/* hero */
.hero{left:0;top:175px;width:1200px;height:691px;background:linear-gradient(160deg,#8cc3d9 0%,#3e9cc8 30%,#6a8b63 55%,#a9784d 80%,#8a5a35 100%)}
.hero-panel{left:125px;top:322px;width:599px;height:305px;background:rgba(32,163,158,.85);border-radius:6px;padding:56px 26px 0 26px;color:var(--white)}
.hero-panel h1{font-size:36px;font-weight:600;line-height:43px;letter-spacing:.3px}
.hero-panel p{margin-top:18px;font-size:15px;line-height:19px;width:500px}
.hero-arrow{top:480px;width:22px;height:22px;border-top:4px solid var(--white);border-left:4px solid var(--white)}

/* headings */
.sec-title{left:0;width:1200px;text-align:center;font-size:38px;font-weight:500;color:var(--teal);letter-spacing:.5px}
.sec-title b{font-weight:700;color:var(--blue)}
.sec-title:after{content:"";display:block;margin:14px auto 0;width:60px;height:3px;background:linear-gradient(90deg,var(--teal) 0 45%,transparent 45% 55%,var(--blue) 55%)}

.btn{display:inline-block;background:var(--teal);color:var(--white);font-weight:600;text-align:center;border-radius:3px}
.btn.blue{background:var(--blue)}

/* about */
.about-art{left:110px;top:930px;width:480px;height:360px;background:linear-gradient(135deg,#bfe6f2 0%,#6cc2df 50%,#2a93c9 100%)}
.about h2{left:645px;top:955px;font-size:40px;font-weight:600;color:var(--blue)}
.about p{position:absolute;left:647px;width:420px;font-size:13px;line-height:17.5px;color:var(--muted)}
.about p.lead{color:var(--ink);font-weight:600}

/* service cards */
.card{background:var(--white);box-shadow:0 3px 14px rgba(0,0,0,.14);overflow:hidden;text-align:center}
.card h3{font-size:21px;font-weight:500;line-height:29px;color:var(--ink)}
.card p{font-size:12.5px;line-height:17px;color:var(--muted);margin-top:10px}
.card .btn{font-size:10px;padding:10px 24px;margin-top:14px}
.card .wave{position:absolute;left:0;bottom:0;width:100%;height:45px;background:linear-gradient(180deg,rgba(255,255,255,0) 0%,#bfe7ee 50%,#4fb6c6 100%)}

/* testimonials */
.tcard{background:var(--white);box-shadow:0 2px 12px rgba(0,0,0,.12)}
.tcard p{font-size:12.5px;line-height:18px;font-style:italic;color:var(--muted);text-align:center}
.quote{font-size:68px;font-weight:700;color:var(--blue);line-height:1;font-family:Georgia,serif}
.stars{color:#f5b400;font-size:15px;letter-spacing:3px}
.dot{top:2487px;width:15px;height:15px;border-radius:50%;background:var(--blue)}

/* plans */
.plan{background:var(--white);box-shadow:0 3px 14px rgba(0,0,0,.14);border-radius:18px 18px 60px 18px;text-align:center}
.plan h3{font-size:28px;font-weight:600;line-height:42px;color:var(--ink)}
.plan .meta{font-size:21px;font-style:italic;color:var(--muted);line-height:34px;margin-top:12px}
.plan .price{color:var(--teal);font-weight:700;font-size:32px;margin-top:12px}
.plan .btn{border-radius:24px;font-size:16px;padding:12px 0;width:150px;margin-top:20px}

/* links */
.badge-card{top:3603px;height:120px;background:var(--white);box-shadow:0 3px 10px rgba(0,0,0,.13);border-radius:6px}
.badge-card span{position:absolute;left:30px;right:30px;top:36px;height:48px;border-radius:6px;background:#d7e3ec}

/* contact */
.touch{top:4027px;width:249px;height:190px;background:linear-gradient(135deg,var(--blue) 0%,var(--teal) 100%);color:var(--white);text-align:center;padding-top:72px}
.touch.mid{background:linear-gradient(135deg,#2aa0cf 0%,#25ad9f 100%)}
.touch.last{background:linear-gradient(135deg,#27a9b6 0%,var(--green) 100%)}
.touch h4{font-size:23px;font-weight:500}
.touch p{font-size:12.5px;line-height:17px;margin:6px 22px 0}
.touch-ico{top:3977px;width:92px;height:92px;border-radius:50%;background:var(--white);box-shadow:0 3px 10px rgba(0,0,0,.15)}
.touch-ico svg{position:absolute;left:26px;top:26px}

/* footer */
.fcol{top:4479px;border-left:3px solid var(--teal);padding-left:20px;height:120px}
.fcol h5{font-size:14px;font-weight:700;color:var(--ink);margin-top:6px}
.fcol a{display:block;font-size:12px;color:var(--ink);text-decoration:none;margin-top:13px}
.finfo{position:absolute;left:30px;font-size:10px;color:var(--muted);line-height:12px}
.fdot{position:absolute;left:0;width:28px;height:28px;border-radius:50%;background:var(--blue)}
.copy{left:0;top:4712px;width:1200px;text-align:center;font-size:10px;color:var(--muted)}
</style>
</head>
<body>

<!-- Top bar -->
<div class="abs topbar">
  <span class="abs follow">FOLLOW US</span>
  <span class="abs social" style="left:201px" aria-hidden="true"></span>
  <span class="abs social" style="left:234px" aria-hidden="true"></span>
  <span class="abs social" style="left:267px" aria-hidden="true"></span>
  <span class="abs social" style="left:300px" aria-hidden="true"></span>
  <span class="abs acct" style="left:752px;border:0">MY ACCOUNT</span>
  <span class="abs acct" style="left:880px">MESSAGE</span>
  <span class="abs acct" style="left:981px">ACCOUNT</span>
</div>

<!-- Header -->
<div class="abs brand-mark" style="left:100px;top:64px;width:30px;height:30px"></div>
<div class="abs brand" style="left:100px;top:126px;font-size:26px">YARDPADDLE</div>

<div class="abs contact-mini" style="left:665px;top:74px"><span class="ico"></span><small>EMAIL US</small>info@yardpaddle.net</div>
<div class="abs contact-mini" style="left:848px;top:74px"><span class="ico"></span><small>CALL US NOW</small>+61 400 512 338</div>
<div class="abs lang"><i></i>ENG &#9662;</div>

<nav class="nav">
  <a class="active" href="#" style="left:424px">HOME</a>
  <a href="#" style="left:498px">ABOUT US</a>
  <a href="#" style="left:599px">SERVICES</a>
  <a href="#" style="left:695px">TESTIMONIALS</a>
  <a href="#" style="left:822px">PRICING</a>
  <a href="#" style="left:909px">PARTNERS</a>
  <a href="#" style="left:1010px">CONTACT US</a>
</nav>

<!-- Hero -->
<div class="abs hero" role="img" aria-label="Backyard above-ground pool with timber deck, flowering shrubs and potted plants"></div>
<span class="abs hero-arrow" style="left:60px;transform:rotate(-45deg)" aria-hidden="true"></span>
<span class="abs hero-arrow" style="left:1116px;transform:rotate(135deg)" aria-hidden="true"></span>
<div class="abs hero-panel">
  <h1>MOBILE SWIMMING LESSONS FOR ALL AGES AND ABILITIES IN ADELAIDE</h1>
  <p>With over 10 years' experience teaching children, teenagers and adults, Rowan brings the skills, knowledge.</p>
</div>
<svg class="band" style="top:740px" width="1200" height="140" viewBox="0 0 1200 140" aria-hidden="true">
  <path d="M0 128 Q600 -20 1200 118 L1200 140 L0 140Z" fill="#fff"/>
  <path d="M0 128 Q600 -20 1200 118" fill="none" stroke="var(--blue)" stroke-width="6"/>
</svg>

<!-- About -->
<section class="about">
  <div class="abs about-art" role="img" aria-label="Illustration of a smiling young swimmer in a pool, framed inside a house outline with a swimmer silhouette"></div>
  <h2 class="abs">ABOUT US</h2>
  <p class="lead" style="top:1011px">Rowan's life, from the very start, revolved around water. His parents met in a swimming club and started him swim­ming before he could walk!</p>
  <p style="top:1080px">From a young age, teaching has come naturally to him and it is something that he truly enjoys. In his spare time, he enjoys hiking with friends and playing Ultimate Frisbee, including helping to coordinate a weekly social league.</p>
  <p style="top:1165px;font-style:italic">Working at Eastbank Swim School (formerly Coastline Swim Eastbank) where, over seven years, Rowan progressed from being a trainee instructor to being a Supervisor as well as performing the role.</p>
  <a class="abs btn" href="#" style="left:647px;top:1262px;width:142px;height:41px;line-height:41px;font-size:12px;text-decoration:none">LEARN MORE</a>
</section>

<svg class="band" style="top:1340px" width="1200" height="110" viewBox="0 0 1200 110" aria-hidden="true">
  <path d="M0 5 Q560 150 1195 5" fill="none" stroke="var(--blue)" stroke-width="6"/>
</svg>

<!-- Services -->
<h2 class="abs sec-title" style="top:1505px">OUR <b>SERVICES</b></h2>

<div class="abs card" style="left:110px;top:1613px;width:299px;height:304px;padding:48px 24px 0">
  <h3>CHILDREN AND TEENAGERS</h3>
  <p>Rowan has over ten years of experience working with frightened four-year-olds right up to teenagers aspiring to club championships, he can help your child(ren) succeed.</p>
  <span class="btn blue">LEARN MORE</span>
  <div class="wave"></div>
</div>
<div class="abs card" style="left:439px;top:1589px;width:326px;height:352px;padding:62px 26px 0">
  <h3>PERSON WITH DISABILITY</h3>
  <p>The aquatic environment can provide freedom, comfort, and confidence to people with a disability. Rowan works with the individual adapting his ap­proach and communication methods to meet their needs.</p>
  <span class="btn blue">LEARN MORE</span>
  <div class="wave"></div>
</div>
<div class="abs card" style="left:798px;top:1618px;width:289px;height:290px;padding:60px 34px 0">
  <h3>ADULTS</h3>
  <p>He works with people of all ages, backgrounds, and cultures. It doesn't matter if you have lived in Australia your whole life or have just arrived recently.</p>
  <span class="btn blue">LEARN MORE</span>
  <div class="wave"></div>
</div>

<svg class="band" style="top:2010px" width="1200" height="120" viewBox="0 0 1200 120" aria-hidden="true">
  <path d="M0 110 Q600 -60 1200 105" fill="none" stroke="var(--blue)" stroke-width="6"/>
</svg>

<!-- Testimonials -->
<h2 class="abs sec-title" style="top:2135px;color:var(--blue);font-weight:600">TESTIMONIALS</h2>

<div class="abs tcard" style="left:-120px;top:2265px;width:356px;height:176px;padding:52px 30px 0 30px">
  <p style="text-align:right">ur adipiscing elit, sed do et dolore magna aliqua. a. Risus commodo viverra s vel facilisis.</p>
  <span class="abs quote" style="left:276px;top:110px">&#8221;</span>
</div>
<div class="abs tcard" style="left:310px;top:2263px;width:584px;height:181px;padding:50px 64px 0">
  <span class="abs quote" style="left:42px;top:24px">&#8220;</span>
  <p>Lorem ipsum dolor sit amet, consectetur adipiscing elit, sed do eiusmod tempor incididunt ut labore et dolore magna aliqua. Quis ipsum suspendisse ultrices gravida. Risus commodo viverra maecenas accumsan lacus vel facilisis.</p>
  <div class="center" style="margin-top:8px"><span class="stars">★★★★★</span> <span style="font-size:11px;color:var(--blue);font-weight:600;margin-left:8px">Sep 09</span></div>
  <span class="abs quote" style="left:500px;top:112px">&#8221;</span>
</div>
<div class="abs" role="img" aria-label="Client portrait" style="left:561px;top:2220px;width:80px;height:80px;border-radius:50%;border:3px solid var(--teal);background:linear-gradient(135deg,#b9d3e3,#5c86a8)"></div>
<div class="abs tcard" style="left:960px;top:2265px;width:300px;height:176px;padding:48px 20px 0 80px">
  <span class="abs quote" style="left:40px;top:24px">&#8220;</span>
  <p style="text-align:left">Lorem ipsum dolor sit am eiusmod tempor incidid Quis ipsum suspendisse u maecenas ac</p>
</div>

<span class="abs dot" style="left:559px;background:#fff;border:2px solid var(--teal)"></span>
<span class="abs dot" style="left:581px"></span>
<span class="abs dot" style="left:603px"></span>
<span class="abs dot" style="left:625px"></span>

<svg class="band" style="top:2595px" width="1200" height="120" viewBox="0 0 1200 120" aria-hidden="true">
  <path d="M0 110 Q600 -60 1200 110" fill="none" stroke="var(--blue)" stroke-width="7"/>
</svg>

<!-- Plans -->
<h2 class="abs sec-title" style="top:2718px">OUR <b>PLANS</b></h2>
<div class="abs center" style="left:0;top:2790px;width:1200px;font-size:13px;font-style:italic;color:var(--ink)">$50 Off Peak - $57.50 Peak (Term 4 wk3 - End Term 4)</div>

<div class="abs plan" style="left:123px;top:2879px;width:290px;height:407px;padding-top:42px">
  <h3>EXTRA TIME</h3>
  <div class="meta">$15.00 (off peak)<br>$17.50 (peak)<br>per 15min<br>above 30 min</div>
  <div class="price">$15.00</div>
  <span class="btn blue">BUY NOW</span>
</div>
<div class="abs plan" style="left:439px;top:2851px;width:326px;height:461px;padding-top:36px">
  <h3 style="font-size:30px;line-height:46px">EXTRA<br>SWIMMERS FREE*</h3>
  <div class="meta" style="font-size:22px;line-height:38px">$15.00 (off peak)<br>$17.50 (peak)<br>per 15min<br>above 30 min</div>
  <div class="price" style="font-size:52px">$55.00</div>
  <span class="btn blue" style="width:168px">BUY NOW</span>
</div>
<div class="abs plan" style="left:798px;top:2875px;width:289px;height:411px;padding-top:36px">
  <h3>LESSONS IN<br>OTHER POOLS</h3>
  <div class="meta" style="margin-top:6px">$15.00 (off peak)<br>$17.50 (peak)<br>per 15min<br>above 30 min</div>
  <div class="price">$106.00</div>
  <span class="btn blue">BUY NOW</span>
</div>

<svg class="band" style="top:3360px" width="1200" height="100" viewBox="0 0 1200 100" aria-hidden="true">
  <path d="M0 10 Q600 140 1200 10" fill="none" stroke="var(--blue)" stroke-width="6"/>
</svg>

<!-- Links -->
<h2 class="abs sec-title" style="top:3520px">OUR <b>LINKS</b></h2>
<div class="abs badge-card" style="left:-170px;width:235px"><span></span></div>
<div class="abs badge-card" style="left:96px;width:236px"><span></span></div>
<div class="abs badge-card" style="left:356px;width:236px"><span></span></div>
<div class="abs badge-card" style="left:617px;width:236px"><span></span></div>
<div class="abs badge-card" style="left:879px;width:234px"><span></span></div>
<div class="abs badge-card" style="left:1143px;width:236px"><span></span></div>

<svg class="band" style="top:3800px" width="1200" height="100" viewBox="0 0 1200 100" aria-hidden="true">
  <defs><linearGradient id="arcTop" x1="0" x2="1"><stop offset="0" stop-color="var(--blue)"/><stop offset="1" stop-color="var(--green)"/></linearGradient></defs>
  <path d="M0 92 Q600 -40 1200 92" fill="none" stroke="url(#arcTop)" stroke-width="8"/>
</svg>

<!-- Get in touch -->
<h2 class="abs sec-title" style="top:3882px">GET IN TOUCH <b>WITH US</b></h2>

<div class="abs touch" style="left:160px"><h4>LOCATION</h4><p>We do the travelling to your home or other pool that's convenient to you</p></div>
<div class="abs touch mid" style="left:475px"><h4>AVAILABILITY</h4><p>We'll work with you to find a time and day that is suitable</p></div>
<div class="abs touch last" style="left:789px"><h4>EMAIL US</h4><p>Use the 'live site' icons on the right or email us</p></div>

<div class="abs touch-ico" style="left:239px">
  <svg width="40" height="40" viewBox="0 0 24 24" aria-hidden="true"><path d="M12 2a7 7 0 0 0-7 7c0 5 7 13 7 13s7-8 7-13a7 7 0 0 0-7-7zm0 9.5A2.5 2.5 0 1 1 12 6.5a2.5 2.5 0 0 1 0 5z" fill="var(--blue)"/></svg>
</div>
<div class="abs touch-ico" style="left:554px">
  <svg width="40" height="40" viewBox="0 0 24 24" aria-hidden="true"><path d="M6.6 10.8a15 15 0 0 0 6.6 6.6l2.2-2.2c.3-.3.7-.4 1-.2 1.1.4 2.3.6 3.6.6.6 0 1 .4 1 1V20c0 .6-.4 1-1 1A17 17 0 0 1 3 4c0-.6.4-1 1-1h3.5c.6 0 1 .4 1 1 0 1.3.2 2.5.6 3.6.1.3 0 .7-.2 1z" fill="var(--blue)"/></svg>
</div>
<div class="abs touch-ico" style="left:868px">
  <svg width="40" height="40" viewBox="0 0 24 24" aria-hidden="true"><path d="M3 5h18v14H3z" fill="var(--blue)"/><path d="M3 5l9 7 9-7" fill="none" stroke="#fff" stroke-width="1.6"/></svg>
</div>

<svg class="band" style="top:4215px" width="1200" height="140" viewBox="0 0 1200 140" aria-hidden="true">
  <defs><linearGradient id="arcBot" x1="0" x2="1"><stop offset="0" stop-color="var(--blue)"/><stop offset="1" stop-color="var(--green)"/></linearGradient></defs>
  <path d="M0 8 Q600 230 1200 8" fill="none" stroke="url(#arcBot)" stroke-width="9"/>
</svg>

<!-- Footer -->
<div class="abs brand-mark" style="left:230px;top:4485px;width:30px;height:30px"></div>
<div class="abs brand" style="left:160px;top:4538px;font-size:28px">YARDPADDLE</div>

<div class="abs fcol" style="left:411px">
  <h5>NAVIGATION</h5>
  <a href="#">HOME</a><a href="#">ABOUT US</a><a href="#">SERVICES</a><a href="#">PRICING</a><a href="#">CONTACT</a>
</div>
<div class="abs fcol" style="left:651px;height:110px">
  <h5 style="font-size:12px">RESOURCES</h5>
  <a href="#">OUR PARTNERS</a><a href="#">TERMS &amp; CONDITIONS</a><a href="#">PRIVACY POLICY</a>
</div>
<div class="abs fcol" style="left:859px;height:40px">
  <h5 style="font-size:12px">CONTACT INFORMATION</h5>
</div>
<div class="abs" style="left:884px;top:4525px;width:240px;height:140px">
  <span class="fdot" style="top:0"></span><span class="finfo" style="top:4px">42 TIDEWATER LANE,<br>GLENELG SA 5045</span>
  <span class="fdot" style="top:44px"></span><span class="finfo" style="top:53px">+61 400 512 338</span>
  <span class="fdot" style="top:88px"></span><span class="finfo" style="top:97px">INFO@YARDPADDLE.NET</span>
</div>

<div class="abs" style="left:0;top:4690px;width:1200px;height:1px;background:var(--line)"></div>
<div class="abs copy">© 2022 YARDPADDLE ALL RIGHT RESERVED</div>

</body>
</html>
```